Consultancy Business Card Design

We need a business card design for a new company based in singapore called FortyOne. FortyOne a boutique consultancy firm offering broad-based business solutions, from conception to re-invention, for ventures from new start-ups to long-running traditional businesses.
Its 2 main divisions (Food & Beverage Operations and Construction & Project Management) have access to a wide range of networks, knowledge bases, and resources to service its clients across numerous diverse sectors. This includes, and is not limited to, construction, F&B, and retail.
We are a company that combines the ambition, boldness and energy of one in the 20s with the dedication, level-headedness and dependability of one entering its 30s. Bridging the experiences of the old with ideals of the young, we draw on the positives of both to create a unique synergy.
We hope to see designs that fits our company profile.
Boutique
FortyOne(Company Name)
Marcus Leow (Name)
Principle Consultant (Title)
F&B and Hospitality (Division)
(+65) 8364 5170 (Contact no.)
marcus@fortyone-example.com.sg (Email)

```html
<!DOCTYPE html>
<html lang="en">
<head>
<meta charset="utf-8">
<title>FortyOne — Business Card</title>
<link rel="stylesheet" href="https://fonts.googleapis.com/css2?family=Lato:wght@300;400;700&display=swap">
<style>
  :root {
    --backdrop: #e9e4dc;
    --card-dark: #2b2b2c;
    --card-dark-deep: #1c1c1d;
    --card-light: #f7f6f4;
    --accent-red: #c8202f;
    --ink: #3a3a3a;
    --ink-soft: #6d6d6d;
    --white: #ffffff;
  }
  * { box-sizing: border-box; margin: 0; padding: 0; }
  html, body {
    width: 705px;
    height: 1200px;
    overflow: hidden;
    background: var(--backdrop);
    font-family: "Lato", Arial, sans-serif;
  }
  .sheet {
    position: relative;
    width: 705px;
    height: 1200px;
  }
  .card {
    position: absolute;
    left: 52px;
    width: 600px;
    height: 343px;
    border-radius: 4px;
    box-shadow: 0 10px 26px rgba(0,0,0,0.22);
    overflow: hidden;
  }

  /* Front */
  .card-front {
    top: 170px;
    background: var(--card-dark);
  }
  .card-front .texture {
    position: absolute;
    inset: 0;
    background: radial-gradient(ellipse at 30% 40%, #3a3a3b 0%, var(--card-dark) 55%, var(--card-dark-deep) 100%);
  }
  .brand-name {
    position: absolute;
    font-weight: 400;
    text-transform: uppercase;
    letter-spacing: 9px;
    line-height: 1;
    white-space: nowrap;
  }
  .card-front .brand-name {
    left: 72px;
    top: 140px;
    font-size: 40px;
    color: var(--white);
  }
  .card-front .division {
    position: absolute;
    left: 74px;
    top: 200px;
    color: var(--white);
    font-size: 14px;
    font-weight: 300;
    letter-spacing: 1px;
  }

  /* Back */
  .card-back {
    top: 660px;
    background: var(--card-light);
  }
  .card-back .frame {
    position: absolute;
    inset: 18px;
    border: 1.5px solid var(--accent-red);
  }
  .card-back .brand-name {
    left: 56px;
    top: 76px;
    font-size: 34px;
    color: var(--ink);
  }
  .person {
    position: absolute;
    left: 56px;
    bottom: 56px;
  }
  .person-name {
    color: var(--accent-red);
    font-size: 22px;
    font-weight: 400;
    margin-bottom: 6px;
  }
  .person-role {
    color: var(--ink-soft);
    font-size: 13px;
    font-weight: 300;
    line-height: 1.5;
  }
  .contact {
    position: absolute;
    right: 56px;
    bottom: 56px;
    list-style: none;
    color: var(--ink);
    font-size: 13px;
    font-weight: 300;
  }
  .contact li {
    display: flex;
    align-items: center;
    justify-content: flex-end;
    gap: 8px;
    line-height: 1.9;
  }
  .contact svg { width: 12px; height: 12px; flex: none; }
</style>
</head>
<body>
  <main class="sheet">
    <section class="card card-front" aria-label="Card front">
      <div class="texture" role="img" aria-label="Faint repeating pattern across dark card face"></div>
      <p class="brand-name">FortyOne</p>
      <p class="division">F&amp;B and Hospitality Division</p>
    </section>

    <section class="card card-back" aria-label="Card back">
      <div class="frame"></div>
      <p class="brand-name">FortyOne</p>
      <div class="person">
        <p class="person-name">Marcus Leow</p>
        <p class="person-role">Principal Consultant<br>F&amp;B and Hospitality</p>
      </div>
      <ul class="contact">
        <li>(+65) 8364 5170
          <svg viewBox="0 0 12 12" aria-hidden="true"><rect width="12" height="12" fill="var(--accent-red)"/><path d="M3.5 2.5l1.5 0 .6 2-1 .7a5 5 0 0 0 2.2 2.2l.7-1 2 .6 0 1.5c-3.5.3-6.3-2.5-6-6z" fill="#fff"/></svg>
        </li>
        <li>marcus@fortyone-example.com.sg
          <svg viewBox="0 0 12 12" aria-hidden="true"><rect width="12" height="12" fill="var(--accent-red)"/><rect x="2.5" y="3.5" width="7" height="5" fill="none" stroke="#fff" stroke-width="0.9"/><path d="M2.5 3.5L6 6.3 9.5 3.5" fill="none" stroke="#fff" stroke-width="0.9"/></svg>
        </li>
      </ul>
    </section>
  </main>
</body>
</html>
```